New Company Business Card Design

I have a new company logo and I want a new business card design. I dont know if the logo file i attached is in the correct format or quality. We are a New York City Specialty construction Firm specializing in high risk out of the box projects. I want a simple and classy business card that people will his card is as crisp as the work his company does.

Target Market(s)

Clients in the heavy construction industry in New York City

Industry/Entity Type

Construction Company

Contact Information for Business Card

Simple Classy - DIFFERENT

Font styles to use
Other font styles liked:
• Mach the logo font in some way

Colors

Designer to choose colors to be used in the design.

Requirements
Must have
• Uniqueness
Nice to have
• Nothing particular - Just different and classy - Timeless
Should not have
• Goofy Shit or Gimmicky shit

```html
<!DOCTYPE html>
<html lang="en">
<head>
<meta charset="utf-8">
<title>Korvane Builders – Business Card</title>
<link rel="stylesheet" href="https://fonts.googleapis.com/css2?family=Montserrat:wght@400;600;700;800&family=Roboto+Slab:wght@700&display=swap">
<style>
  :root {
    --backdrop: #d6d6d6;
    --charcoal: #2e3136;
    --paper: #ececea;
    --accent-blue: #1e9ad6;
    --brand-blue: #1a5fa0;
    --ink: #3a3b3d;
    --white: #ffffff;
  }
  * { margin: 0; padding: 0; box-sizing: border-box; }
  html, body {
    width: 1200px; height: 1000px; overflow: hidden;
    background: var(--backdrop);
    font-family: "Montserrat", sans-serif;
  }
  .card {
    position: absolute; left: 250px;
    width: 700px; height: 400px;
    box-shadow: 0 10px 30px rgba(0,0,0,0.18);
    overflow: hidden;
  }
  /* Front */
  .card--front { top: 60px; background: var(--charcoal); }
  .front__brand {
    position: absolute; left: 0; right: 0; top: 160px;
    text-align: center; color: var(--white);
    font-weight: 800; font-size: 40px; letter-spacing: 1px;
  }
  .front__web {
    position: absolute; left: 0; right: 0; top: 250px;
    text-align: center; color: var(--accent-blue);
    font-weight: 600; font-size: 19px;
  }
  /* Back */
  .card--back { top: 540px; background: var(--paper); }
  .back__brand {
    position: absolute; left: 40px; top: 180px;
    color: var(--brand-blue);
    font-weight: 800; font-size: 30px; line-height: 1.1;
    width: 230px;
  }
  .name-band {
    position: absolute; left: 285px; right: 0; top: 62px; height: 78px;
    background: var(--charcoal);
  }
  .name-band__accent {
    position: absolute; right: 0; top: 0; width: 22px; height: 100%;
    background: var(--accent-blue);
  }
  .holder__name {
    position: absolute; left: 22px; top: 10px;
    font-family: "Roboto Slab", serif; font-weight: 700;
    font-size: 27px; color: var(--white);
  }
  .holder__title {
    position: absolute; left: 24px; top: 47px;
    font-weight: 700; font-size: 14px; letter-spacing: 1px;
    color: var(--white);
  }
  .contact {
    position: absolute; left: 310px; top: 165px;
    color: var(--ink); font-size: 17px; line-height: 25px;
  }
  .contact__address { margin-bottom: 12px; }
  .contact__row { display: flex; align-items: center; gap: 12px; }
  .contact__icon { width: 16px; height: 16px; flex: none; }
  .contact__row--web { font-weight: 700; font-size: 18px; margin-top: 4px; }
</style>
</head>
<body>

<section class="card card--front" aria-label="Card front">
  <div class="front__brand">Korvane Builders, Inc.</div>
  <div class="front__web">www.korvane.com</div>
</section>

<section class="card card--back" aria-label="Card back">
  <div class="back__brand">Korvane Builders, Inc.</div>

  <div class="name-band">
    <div class="holder__name">Marco T. Velluti</div>
    <div class="holder__title">BUSINESS DEVELOPMENT</div>
    <div class="name-band__accent"></div>
  </div>

  <div class="contact">
    <div class="contact__address">
      418 Harbor Line Street<br>
      Linden, New Jersey 07036
    </div>
    <div class="contact__row">
      <svg class="contact__icon" viewBox="0 0 16 16" aria-hidden="true"><path d="M4 1.5l2.2 3-1.4 1.6c.8 1.8 2.3 3.3 4.1 4.1l1.6-1.4 3 2.2-1.2 2.6C6.8 13.5 2.5 9.2 1.4 2.7z" fill="none" stroke="var(--accent-blue)" stroke-width="1.4" stroke-linejoin="round"/></svg>
      <span>555-014-2281</span>
    </div>
    <div class="contact__row">
      <svg class="contact__icon" viewBox="0 0 16 16" aria-hidden="true"><rect x="4" y="1" width="8" height="14" rx="1.5" fill="none" stroke="var(--accent-blue)" stroke-width="1.4"/><line x1="7" y1="12.5" x2="9" y2="12.5" stroke="var(--accent-blue)" stroke-width="1.4"/></svg>
      <span>555-017-3390</span>
    </div>
    <div class="contact__row">
      <svg class="contact__icon" viewBox="0 0 16 16" aria-hidden="true"><rect x="1" y="3" width="14" height="10" rx="1" fill="none" stroke="var(--accent-blue)" stroke-width="1.4"/><path d="M1.5 3.5L8 9l6.5-5.5" fill="none" stroke="var(--accent-blue)" stroke-width="1.4"/></svg>
      <span>MARCO@korvane.com</span>
    </div>
    <div class="contact__row contact__row--web">
      <svg class="contact__icon" viewBox="0 0 16 16" aria-hidden="true"><circle cx="8" cy="8" r="7" fill="var(--accent-blue)"/><path d="M1 8h14M8 1c-2.5 2-2.5 12 0 14M8 1c2.5 2 2.5 12 0 14" fill="none" stroke="var(--white)" stroke-width="1"/></svg>
      <span>www.korvane.com</span>
    </div>
  </div>
</section>

</body>
</html>
```